Actors Postcard Design

I need a postcard designed for me. I am an actor, voice over artist and technical adviser for tv, film and videogames. I am open to color ideas. My photos are in black and white so something to make those stand out a bit. Masculine colors like dark blue etc..I have seen some of your designs with 3 photos which I liked. Perhaps a 2-3 photo scheme. Back of postcard to contain my resume. Want it to look professional and not cartoonish (since I mentioned video games). Front to have photos and job title and contact info

Please take my color direction lightly, I am open to all color schemes. light or dark. You are the professionals. Am looking forward to seeing what all of you come up with. Thanks

Tv

```html
<!DOCTYPE html>
<html lang="en">
<head>
<meta charset="utf-8">
<title>Marek "Mack" Kowalczyk – Actor Postcard</title>
<link href="https://fonts.googleapis.com/css2?family=Questrial&family=Montserrat:wght@700&display=swap" rel="stylesheet">
<style>
  :root {
    --ink: #000000;
    --paper: #ffffff;
    --accent: #12acd9;
    --photo-light: #8a8a8a;
    --photo-mid: #4a4a4a;
    --photo-dark: #141414;
    --fold: #d9d9d9;
    --corner-text: #1a1a1a;
  }
  html, body {
    margin: 0;
    padding: 0;
    overflow: hidden;
    background: var(--ink);
  }
  .postcard {
    position: relative;
    width: 1200px;
    height: 924px;
    overflow: hidden;
    background: var(--ink);
    font-family: "Questrial", "Century Gothic", sans-serif;
    color: var(--paper);
  }
  .headshot {
    position: absolute;
    left: 0;
    top: 0;
    width: 820px;
    height: 924px;
    background:
      radial-gradient(ellipse 300px 380px at 290px 400px, var(--photo-light) 0%, var(--photo-mid) 55%, transparent 100%),
      linear-gradient(90deg, var(--photo-mid) 0%, var(--photo-dark) 65%, var(--ink) 100%);
  }
  .page-curl {
    position: absolute;
    right: 0;
    top: 0;
    width: 310px;
    height: 210px;
  }
  .corner-note {
    position: absolute;
    right: 28px;
    top: 20px;
    margin: 0;
    font-size: 21px;
    line-height: 28px;
    text-align: center;
    color: var(--corner-text);
    letter-spacing: 0.5px;
  }
  .name {
    position: absolute;
    left: 520px;
    width: 630px;
    top: 258px;
    margin: 0;
    text-align: center;
    font-weight: 400;
    font-size: 66px;
    line-height: 76px;
    letter-spacing: 2px;
  }
  .name .nickname {
    font-family: "Montserrat", sans-serif;
    font-weight: 700;
    color: var(--accent);
    font-size: 64px;
  }
  .contact {
    position: absolute;
    left: 520px;
    width: 630px;
    top: 472px;
    text-align: center;
  }
  .contact .phone {
    display: flex;
    justify-content: center;
    align-items: center;
    gap: 6px;
    font-size: 64px;
    line-height: 80px;
    margin: 0;
  }
  .contact .phone svg { width: 34px; height: 44px; }
  .contact .email {
    margin: 4px 0 0;
    font-size: 28px;
    color: var(--accent);
    letter-spacing: 0.5px;
  }
  .stats {
    position: absolute;
    left: 560px;
    top: 678px;
    display: flex;
    gap: 0;
    margin: 0;
    padding: 0;
    list-style: none;
  }
  .stat {
    width: 155px;
    text-align: center;
  }
  .stat:nth-child(2) { width: 160px; }
  .stat .icon {
    display: block;
    width: 100px;
    height: 100px;
    margin: 0 auto;
  }
  .stat .label {
    display: block;
    margin-top: 14px;
    font-size: 27px;
    line-height: 32px;
  }
  .stat .value {
    display: block;
    font-family: "Montserrat", sans-serif;
    font-weight: 700;
    font-size: 25px;
    line-height: 36px;
    color: var(--accent);
  }
</style>
</head>
<body>
<main class="postcard">
  <div class="headshot" role="img" aria-label="Black and white headshot of the actor, smiling, in a collared shirt against dark foliage"></div>

  <svg class="page-curl" viewBox="0 0 310 210" aria-hidden="true">
    <path d="M0 0 H310 V150 C250 150 215 175 195 205 C175 110 90 40 0 0 Z" fill="var(--accent)"/>
    <path d="M0 0 C90 40 175 110 195 205 C170 150 120 130 95 95 C70 60 35 25 0 0 Z" fill="var(--fold)"/>
    <path d="M0 0 C35 25 70 60 95 95 C120 130 170 150 195 205 C150 160 100 140 60 90 Z" fill="var(--paper)"/>
  </svg>
  <p class="corner-note">DETAILS<br>ON BACK</p>

  <h1 class="name">MAREK <span class="nickname">“MACK”</span><br>KOWALCZYK</h1>

  <div class="contact">
    <p class="phone">
      <svg viewBox="0 0 34 44" aria-hidden="true">
        <path d="M10 4 C4 6 2 12 3 22 C4 32 9 39 14 41 L18 40 L16 30 L12 30 C10 26 9 18 11 14 L15 13 L15 3 Z" fill="var(--paper)"/>
      </svg>
      503-555-0148
    </p>
    <p class="email">Marekkowalczyk@inboxmail.com</p>
  </div>

  <ul class="stats">
    <li class="stat">
      <svg class="icon" viewBox="0 0 100 100" aria-hidden="true">
        <circle cx="50" cy="50" r="47" fill="none" stroke="var(--accent)" stroke-width="3"/>
        <g fill="none" stroke="var(--paper)" stroke-width="3">
          <circle cx="40" cy="29" r="6"/>
          <path d="M30 40 H50 V58 H46 V74 H34 V58 H30 Z"/>
          <path d="M58 27 H72 M58 35 H68 M58 43 H72 M58 51 H68 M58 59 H72 M58 67 H68 M58 75 H72"/>
        </g>
      </svg>
      <span class="label">HEIGHT</span>
      <span class="value">6’0”</span>
    </li>
    <li class="stat">
      <svg class="icon" viewBox="0 0 100 100" aria-hidden="true">
        <circle cx="50" cy="50" r="47" fill="none" stroke="var(--accent)" stroke-width="3"/>
        <g fill="none" stroke="var(--paper)" stroke-width="3">
          <rect x="27" y="27" width="46" height="46" rx="7"/>
          <rect x="36" y="46" width="28" height="18" rx="2"/>
          <path d="M40 38 A10 10 0 0 1 60 38 Z" fill="var(--paper)"/>
        </g>
      </svg>
      <span class="label">WEIGHT</span>
      <span class="value">180</span>
    </li>
    <li class="stat">
      <svg class="icon" viewBox="0 0 100 100" aria-hidden="true">
        <circle cx="50" cy="50" r="47" fill="none" stroke="var(--accent)" stroke-width="3"/>
        <path d="M32 48 C28 30 40 20 54 22 C64 18 72 26 68 34 C70 40 69 45 68 48 C66 40 60 36 52 38 C44 40 38 40 34 46 Z" fill="var(--paper)"/>
        <path d="M33 48 C33 62 40 72 50 72 C60 72 67 62 67 48" fill="none" stroke="var(--paper)" stroke-width="3"/>
      </svg>
      <span class="label">HAIR</span>
      <span class="value">BLOND</span>
    </li>
    <li class="stat">
      <svg class="icon" viewBox="0 0 100 100" aria-hidden="true">
        <circle cx="50" cy="50" r="47" fill="none" stroke="var(--accent)" stroke-width="3"/>
        <path d="M18 50 C30 34 70 34 82 50 C70 66 30 66 18 50 Z" fill="var(--paper)"/>
        <circle cx="50" cy="50" r="11" fill="var(--ink)"/>
        <circle cx="50" cy="50" r="5" fill="var(--paper)"/>
      </svg>
      <span class="label">EYES</span>
      <span class="value">GREEN</span>
    </li>
  </ul>
</main>
</body>
</html>
```